QUICK: Fresh Ideas for New Home Page Design!

Simply improve on our home page design and provide PSD file.

We are Sunward Coverage, a trusted health insurance comparison site to make shopping and enrolling in Carewell easy. We are certified agents for Pacific Shield Exchange, the state's health insurance marketplace (logo attached).

Use flat UI colors.

Looking for a fun design. Reference websites are:
www.plumvista.com
www.hibrindle.com
www.tolmex.com
www.findcanopy.com
www.trymeadowcoverplan.com

Target Market(s)

Individuals ages 18 - 64 shopping for health insurance for themselves and/or their family members. California residents. Don't have health insurance and want it or have it and looking to change.

Industry/Entity Type

Shopping

Font styles to use
Sans Serif

Colors
faed22
33a6d7
33b7a4

Requirements
Must have
• No stock photos. No medical or doctor images or photos. Use images of families. Friendly. Modern fonts and flat UI colors.
Nice to have
• Create a mock-up logo for Sunward Coverage.
Should not have
• No stock looking photos or images

```html
<!DOCTYPE html>
<html lang="en">
<head>
<meta charset="utf-8">
<title>Pacific Shield Exchange – Home</title>
<link href="https://fonts.googleapis.com/css2?family=Questrial&family=Open+Sans:wght@400;600;700&display=swap" rel="stylesheet">
<style>
:root{
  --teal:#1fb3cb;
  --teal-dark:#1596ab;
  --yellow:#e9b321;
  --green:#2f6b57;
  --green-btn:#3b8a73;
  --olive:rgba(150,128,30,.88);
  --ink:#333;
  --grey:#777;
  --light:#f4f4f4;
  --footer:#3d3a3f;
  --footer-deep:#2e2b30;
  --white:#fff;
}
*{margin:0;padding:0;box-sizing:border-box}
html,body{width:1200px;height:3082px;overflow:hidden}
body{position:relative;font-family:"Open Sans",Arial,sans-serif;color:var(--ink);background:var(--white)}

/* header */
.site-header{position:absolute;left:0;top:0;width:1200px;height:127px}
.brand{position:absolute;left:123px;top:28px;display:flex;align-items:center;gap:14px}
.brand-mark{width:64px;height:64px;border-radius:50%;background:var(--teal)}
.brand-name{font-family:"Questrial",sans-serif;font-size:26px;line-height:28px;color:var(--green);width:240px}
.util-links{position:absolute;right:124px;top:14px;font-size:11px;color:#555;letter-spacing:.5px}
.phone{position:absolute;right:124px;top:70px;font-size:26px;color:#333;display:flex;align-items:center;gap:8px}
.main-nav{position:absolute;left:0;top:127px;width:1200px;height:54px;background:linear-gradient(var(--teal),var(--teal-dark))}
.main-nav ul{list-style:none;display:flex;position:absolute;left:123px;top:0;height:54px}
.main-nav li{color:#fff;font-size:15px;font-weight:600;padding:0 15px;line-height:54px;border-right:1px solid rgba(255,255,255,.35)}
.main-nav li:last-child{border-right:none}

/* hero */
.hero{position:absolute;left:0;top:181px;width:1200px;height:497px;background:linear-gradient(135deg,#6f8f3a 0%,#9bb25a 35%,#7a6a4c 70%,#4c5a2c 100%)}
.hero-box{position:absolute;left:298px;top:168px;width:602px;height:176px;background:rgba(60,60,50,.55);text-align:center;color:#fff}
.hero-box h1{font-family:"Questrial",sans-serif;font-weight:400;font-size:36px;margin-top:26px;letter-spacing:.5px;white-space:nowrap}
.hero-box p{font-size:19px;margin-top:2px;letter-spacing:.5px;white-space:nowrap}
.hero-btns{display:flex;justify-content:center;gap:12px;margin-top:16px}
.btn{display:inline-block;color:#fff;font-size:13px;font-weight:700;padding:0 24px;line-height:34px;letter-spacing:.5px;white-space:nowrap}
.btn-teal{background:var(--teal)}
.btn-yellow{background:var(--yellow)}
.btn-green{background:var(--green-btn)}
.slide-arrow{position:absolute;width:30px;height:60px}

.quick-bar{position:absolute;left:0;top:678px;width:1200px;height:76px;background:var(--olive);display:flex}
.quick-bar .item{flex:1;display:flex;align-items:center;justify-content:center;gap:16px;color:#fff;font-weight:700;font-size:18px;border-right:1px solid rgba(255,255,255,.3)}
.quick-bar .item:last-child{border-right:none}

/* stats */
.stats{position:absolute;left:0;top:754px;width:1200px;height:331px}
.stats h2{position:absolute;left:123px;top:62px;font-family:"Questrial",sans-serif;font-weight:400;font-size:36px;color:#444}
.stats h3{position:absolute;left:123px;top:110px;font-family:"Questrial",sans-serif;font-weight:400;font-size:23px;color:#888}
.stats p{position:absolute;left:123px;top:152px;width:400px;font-size:12.5px;line-height:22px;color:#888}
.pie{position:absolute;top:76px;width:130px;text-align:center}
.pie .label{font-size:12px;line-height:17px;color:#666;margin-top:6px}

/* help section */
.help{position:absolute;left:0;top:1085px;width:1200px;height:450px;background:linear-gradient(180deg,#5a564a 0%,#6e6a58 50%,#4d4a3e 100%)}
.help h2{position:absolute;left:0;width:1200px;top:56px;text-align:center;font-family:"Questrial",sans-serif;font-weight:400;font-size:32px;color:#fff}
.help-item{position:absolute;top:150px;width:220px;text-align:center;color:#fff;font-size:15px;line-height:24px}
.help-circle{width:110px;height:110px;border-radius:50%;background:#2b2a26;border:4px solid var(--yellow);margin:0 auto 14px;display:flex;align-items:center;justify-content:center}
.help .btn{position:absolute;left:495px;top:364px;width:189px;padding:0;text-align:center;line-height:44px;font-size:14px}

/* premiums */
.premiums{position:absolute;left:0;top:1535px;width:1200px;height:664px;background:var(--light)}
.premiums h2{position:absolute;left:0;width:1200px;top:60px;text-align:center;font-family:"Questrial",sans-serif;font-weight:400;font-size:31px;color:#444}
.card{position:absolute;width:181px;height:189px;background:#fff;border:1px solid #e2e2e2;text-align:center}
.card .avatar{width:104px;height:104px;border-radius:50%;margin:16px auto 10px;background:linear-gradient(135deg,#cfe3ee,#e8d8c8);border:3px solid #fff;box-shadow:0 0 0 1px #ddd}
.card .who{font-size:14px;color:#555}
.card .price{font-size:14px;color:var(--teal);margin-top:2px}
.enrolled{position:absolute;left:200px;top:587px;font-family:"Questrial",sans-serif;font-size:18px;color:#999;white-space:nowrap}
.premiums .btn{position:absolute;left:786px;top:580px;width:175px;padding:0;text-align:center;line-height:38px}

/* testimonials */
.testimonials{position:absolute;left:0;top:2199px;width:1200px;height:318px;background:var(--teal)}
.testimonials h2{position:absolute;left:320px;width:580px;top:52px;text-align:center;font-family:"Questrial",sans-serif;font-weight:400;font-size:34px;color:#fff}
.quote{position:absolute;left:226px;top:118px;width:560px;color:#fff;font-size:12px;line-height:24px;font-style:italic}
.quote .mark{font-size:40px;font-family:Georgia,serif;font-style:normal;position:absolute;left:-4px;top:-12px}
.quote .by{font-weight:700;font-style:normal}
.testimonial-photo{position:absolute;left:812px;top:20px;width:185px;height:298px;background:linear-gradient(180deg,#e9d7c4,#f4f1ec);border-radius:92px 92px 0 0}

/* partners */
.partners{position:absolute;left:0;top:2517px;width:1200px;height:196px}
.partners h2{position:absolute;left:0;width:1200px;top:36px;text-align:center;font-family:"Questrial",sans-serif;font-weight:400;font-size:25px;color:#999}
.partner{position:absolute;top:124px;display:flex;align-items:center;gap:6px;font-size:14px;font-weight:600;color:#4a4a7a;transform:translateX(-50%);white-space:nowrap}
.partner .dot{width:14px;height:14px;border-radius:50%;background:#8aa0c8}

/* footer */
.site-footer{position:absolute;left:0;top:2713px;width:1200px;height:312px;background:var(--footer);color:#fff}
.f-col{position:absolute;top:52px}
.f-col h4{font-weight:400;font-size:17px;margin-bottom:12px}
.f-col ul{list-style:none}
.f-col li{font-size:12px;line-height:26.5px;color:#ddd}
.f-divider{position:absolute;top:52px;width:1px;height:210px;background:#59565b}
.post-title{font-size:13px;color:#eee}
.post-text{font-size:11px;line-height:16px;color:#aaa;width:340px}
.post-more{font-size:10px;font-weight:700;color:var(--yellow);margin-bottom:14px}
.contact-line{font-size:12.5px;line-height:26px;color:#ddd}
.contact-phone{font-size:22px;line-height:32px}
.socials{display:flex;gap:6px;margin-top:8px}
.socials span{width:28px;height:28px;border-radius:50%;background:#fff}
.bottom-bar{position:absolute;left:0;top:3025px;width:1200px;height:57px;background:var(--footer-deep);color:#888;font-size:10px;line-height:57px;padding-left:140px}
</style>
</head>
<body>

<header class="site-header">
  <div class="brand"><span class="brand-mark"></span><span class="brand-name">Pacific Shield Exchange</span></div>
  <div class="util-links">ACCOUNT LOGIN &nbsp;|&nbsp; CONTACT</div>
  <div class="phone">
    <svg width="26" height="26" viewBox="0 0 26 26"><circle cx="13" cy="13" r="11" fill="none" stroke="#1fb3cb" stroke-width="2"/><path d="M9 8c0 5 4 9 9 9l1-2-3-2-1 1c-2-1-3-2-4-4l1-1-2-3z" fill="#1fb3cb"/></svg>
    800-555-0142
  </div>
</header>

<nav class="main-nav">
  <ul>
    <li>HOME</li><li>HEALTH PLANS</li><li>HEALTH BENEFITS</li><li>AFFORDABLE OPTIONS</li><li>EMPLOYERS</li><li>ABOUT US</li><li>RESOURCES</li>
  </ul>
</nav>

<section class="hero" role="img" aria-label="Family with young children relaxing on the grass outdoors">
  <svg class="slide-arrow" style="left:78px;top:210px" viewBox="0 0 30 60"><path d="M24 4 6 30l18 26" fill="none" stroke="#fff" stroke-width="2.5"/></svg>
  <svg class="slide-arrow" style="left:1092px;top:210px" viewBox="0 0 30 60"><path d="M6 4l18 26L6 56" fill="none" stroke="#fff" stroke-width="2.5"/></svg>
  <div class="hero-box">
    <h1>MAURIS VEL LACUS VITAE FELIS</h1>
    <p>ETIAM EST NUNC VENENATIS IN TRISTIQUE</p>
    <div class="hero-btns"><span class="btn btn-teal">APPLY NOW</span><span class="btn btn-yellow">FIND PLANS</span><span class="btn btn-green">RENEW NOW</span></div>
  </div>
</section>

<div class="quick-bar">
  <div class="item"><svg width="34" height="34" viewBox="0 0 34 34" fill="none" stroke="#fff" stroke-width="2.5"><rect x="3" y="3" width="28" height="28" rx="3"/><path d="M3 12h28M3 21h28M12 3v28M21 3v28"/></svg>DO I AGREE</div>
  <div class="item"><svg width="36" height="32" viewBox="0 0 36 32" fill="none" stroke="#fff" stroke-width="2.5"><path d="M3 12 7 3h22l4 9H3zM5 12v17h26V12M14 29v-9h8v9"/></svg>EMPLOYERS</div>
  <div class="item"><svg width="36" height="36" viewBox="0 0 36 36" fill="none" stroke="#fff" stroke-width="2.5"><path d="M6 26a14 14 0 1 1 24 0"/><path d="M14 14a4 4 0 1 1 5 4v3"/><circle cx="19" cy="26" r="1.5" fill="#fff"/></svg>GET HELP</div>
  <div class="item"><svg width="32" height="34" viewBox="0 0 32 34" fill="none" stroke="#fff" stroke-width="2.5"><rect x="3" y="10" width="26" height="21"/><path d="M10 10V6a6 6 0 0 1 12 0v4"/></svg>SHOP + COMPARE</div>
</div>

<section class="stats">
  <h2>Mauris vel lacus vitae felis</h2>
  <h3>Etiam est nunc venenatis in tristique</h3>
  <p>Consequat id duo, cu aeterno indoctum his. Ornatus docendi instructior ex sea. Ei sonet aeterno malorum ius, natum dolorum invenire mea ex, ne eius suscipiantur duo. Pro quando dictas ad. Dolores urbanitas interesset his teele uewan dashen.</p>

  <div class="pie" style="left:615px">
    <svg width="124" height="124" viewBox="0 0 130 130"><circle cx="65" cy="65" r="60" fill="#e6e6e6"/><path d="M65 65V5A60 60 0 1 1 17.4 28.5Z" fill="#e9b321"/><text x="65" y="76" text-anchor="middle" font-family="Questrial,sans-serif" font-size="28" fill="#fff">87%</text></svg>
    <div class="label">of People Qualify<br>for Subsidies</div>
  </div>
  <div class="pie" style="left:775px">
    <svg width="124" height="124" viewBox="0 0 130 130"><circle cx="65" cy="65" r="60" fill="#e6e6e6"/><path d="M65 65V5A60 60 0 1 1 14.2 33.1Z" fill="#1fb3cb"/><text x="65" y="76" text-anchor="middle" font-family="Questrial,sans-serif" font-size="28" fill="#fff">86%</text></svg>
    <div class="label">Average Discount<br>After Subsides</div>
  </div>
  <div class="pie" style="left:936px">
    <svg width="124" height="124" viewBox="0 0 130 130"><circle cx="65" cy="65" r="60" fill="#e6e6e6"/><path d="M65 65V5A60 60 0 1 1 8.0 46.5Z" fill="#2f6b57"/><text x="65" y="76" text-anchor="middle" font-family="Questrial,sans-serif" font-size="28" fill="#fff">82%</text></svg>
    <div class="label">Average Monthly<br>Premium</div>
  </div>
</section>

<section class="help" role="img" aria-label="Father carrying his child beside a lake, dimmed behind the text">
  <h2>Health Insurance doesn't have to be Complicated</h2>
  <svg class="slide-arrow" style="left:86px;top:168px" viewBox="0 0 30 60"><path d="M24 4 6 30l18 26" fill="none" stroke="#fff" stroke-width="2.5"/></svg>
  <svg class="slide-arrow" style="left:1086px;top:168px" viewBox="0 0 30 60"><path d="M6 4l18 26L6 56" fill="none" stroke="#fff" stroke-width="2.5"/></svg>
  <div class="help-item" style="left:137px"><div class="help-circle"><svg width="50" height="50" viewBox="0 0 50 50" fill="none" stroke="#e9b321" stroke-width="5"><circle cx="20" cy="20" r="13"/><path d="M30 30l14 14"/></svg></div>We Help you get<br>Financial Assistance</div>
  <div class="help-item" style="left:367px"><div class="help-circle"><svg width="50" height="50" viewBox="0 0 50 50" fill="none" stroke="#e9b321" stroke-width="3"><path d="M8 6h24v38H8z"/><path d="M38 10 22 30l-2 6 6-2 16-20z"/></svg></div>We Help you choose<br>the right plan</div>
  <div class="help-item" style="left:607px"><div class="help-circle"><svg width="50" height="50" viewBox="0 0 50 50" fill="none" stroke="#e9b321" stroke-width="3"><circle cx="25" cy="22" r="16"/><path d="M12 36h26M14 42h22M20 22h10"/></svg></div>We make sure you get<br>the Best Deal possible</div>
  <div class="help-item" style="left:835px"><div class="help-circle"><svg width="50" height="50" viewBox="0 0 50 50" fill="none" stroke="#e9b321" stroke-width="3"><path d="M6 10h38v24H22l-10 8v-8H6z"/><circle cx="16" cy="22" r="2" fill="#e9b321"/><circle cx="25" cy="22" r="2" fill="#e9b321"/><circle cx="34" cy="22" r="2" fill="#e9b321"/></svg></div>We Help you<br>Enroll</div>
  <span class="btn btn-yellow">LET US HELP YOU</span>
</section>

<section class="premiums">
  <h2>Real Monthly Premiums, Real People</h2>
  <div class="card" style="left:201px;top:132px"><div class="avatar" role="img" aria-label="Portrait of a young man"></div><div class="who">Male, 27</div><div class="price">$28.12</div></div>
  <div class="card" style="left:401px;top:132px"><div class="avatar" role="img" aria-label="Portrait of a woman"></div><div class="who">Female, 43</div><div class="price">$82.33</div></div>
  <div class="card" style="left:600px;top:132px"><div class="avatar" role="img" aria-label="Portrait of an older man"></div><div class="who">Male, 62</div><div class="price">$35.34</div></div>
  <div class="card" style="left:797px;top:132px"><div class="avatar" role="img" aria-label="Mother with her two children"></div><div class="who">Single Mom, 2 kids</div><div class="price">$37.76</div></div>
  <div class="card" style="left:201px;top:343px"><div class="avatar" role="img" aria-label="Family of four"></div><div class="who">Family of 4</div><div class="price">$132.44</div></div>
  <div class="card" style="left:401px;top:343px"><div class="avatar" role="img" aria-label="Married couple"></div><div class="who">Married Couple</div><div class="price">$89.12</div></div>
  <div class="card" style="left:600px;top:343px"><div class="avatar" role="img" aria-label="Family of three"></div><div class="who">Family of 3</div><div class="price">$56.12</div></div>
  <div class="card" style="left:797px;top:343px"><div class="avatar" role="img" aria-label="Portrait of an older woman"></div><div class="who">Female, 57</div><div class="price">$77.67</div></div>
  <div class="enrolled">Over 1,395,929 People Have Enrolled in Pacific Shield Exchange.</div>
  <span class="btn btn-teal">GET A QUOTE NOW</span>
</section>

<section class="testimonials">
  <svg class="slide-arrow" style="left:98px;top:128px;width:20px;height:40px" viewBox="0 0 20 40"><path d="M16 4 4 20l12 16" fill="none" stroke="#0e7f92" stroke-width="2.5"/></svg>
  <svg class="slide-arrow" style="left:1100px;top:128px;width:20px;height:40px" viewBox="0 0 20 40"><path d="M4 4l12 16L4 36" fill="none" stroke="#0e7f92" stroke-width="2.5"/></svg>
  <h2>Testimonials</h2>
  <div class="quote"><span class="mark">“</span><div style="padding-left:30px">Nam a malesuada libero. Duis sodales et libero vel interdum. Interdum et malesuada fames ac ante ipsum primis in faucibus. Donec lobortis dui tortor, eu lobortis felis mattis nec. Sed justo quam, luctus eu mauris eget, euismod dapibus sem. Sed tempus feugiat ante, at ornare libero volutpat sed. ”<br><span class="by">Marisol - City</span></div></div>
  <div class="testimonial-photo" role="img" aria-label="Smiling young woman in a white top"></div>
</section>

<section class="partners">
  <h2>Choice for affordable Health Coverage</h2>
  <div class="partner" style="left:212px"><span class="dot"></span>Harborline Health</div>
  <div class="partner" style="left:388px"><span class="dot"></span>Keystone Care</div>
  <div class="partner" style="left:552px"><span class="dot"></span>Brightpath</div>
  <div class="partner" style="left:692px"><span class="dot"></span>Westvale Health</div>
  <div class="partner" style="left:847px"><span class="dot"></span>Corvana</div>
  <div class="partner" style="left:1013px"><span class="dot"></span>Meadowlark Plan</div>
</section>

<footer class="site-footer">
  <div class="f-col" style="left:136px">
    <h4>QUICK LINKS</h4>
    <ul><li>Eligibility Chart</li><li>Standard Benefits</li><li>Enhanced Benefits</li><li>Household Income Worksheet</li><li>Agent Delegation</li><li>Service Appointment Authorization</li><li>Appeals Process</li></ul>
  </div>
  <div class="f-divider" style="left:380px"></div>
  <div class="f-col" style="left:417px">
    <h4>RECENT BLOG POST</h4>
    <div class="post-title">Mauris vel lacus vitae</div>
    <div class="post-text">Etiam est nunc venenatis in tristique eu imperdiet ac nisl. Cum sociis natoque penatibus et magnis dis parturient</div>
    <div class="post-more">READ FULL STORY</div>
    <div class="post-title">Etiam est nunc venenatis</div>
    <div class="post-text">Etiam est nunc venenatis in tristique eu imperdiet ac nisl. Cum sociis natoque penatibus et magnis dis parturient</div>
    <div class="post-more">READ FULL STORY</div>
  </div>
  <div class="f-divider" style="left:775px"></div>
  <div class="f-col" style="left:822px">
    <h4>CONTACT US</h4>
    <div class="contact-line">42 Linden Avenue #3B</div>
    <div class="contact-line">Fresno 93701 CA</div>
    <div class="contact-line contact-phone">555.014.2290</div>
    <div class="contact-line">hello@sunwardcoverage.com</div>
    <div class="socials"><span></span><span></span><span></span><span></span></div>
  </div>
</footer>
<div class="bottom-bar">© 2014 Company Name &nbsp;All right reserved &nbsp;Term of Use</div>

</body>
</html>
```